Redesign BrightCoinDesk.info

We are unhappy with the design and layout of our current site www.BrightCoinDesk.info
We would like the following pages redesigned using a consistent style.
http://www.brightcoindesk.info/
http://www.brightcoindesk.info/live_forex_signals.php
http://www.brightcoindesk.info/forex-signal/71/TQ-Overdrive.html
http://www.brightcoindesk.info/broker_rebates.php
http://www.brightcoindesk.info/contact.php
Ideally we would also like the contractor to be able to code it into HTML.
We currently like our colour scheme of black, blue and grey.
Updates
We would like to consider a logo redesign. We're happy to pay a $30 bonus for a new logo.
Target Market(s)
80% males between 25 and 50 years old
Industry/Entity Type
Contractor

```html
<!DOCTYPE html>
<html lang="en">
<head>
<meta charset="utf-8">
<title>BrightCoinDesk.info – Follow Professional Traders</title>
<link rel="stylesheet" href="https://fonts.googleapis.com/css2?family=Roboto+Condensed:wght@400;700&family=Arimo:wght@400&family=Open+Sans:wght@400;600&display=swap">
<style>
:root{
  --page-bg:#e9e9e9;
  --page-top:#f4f4f4;
  --panel:#ffffff;
  --line:#d8d8d8;
  --ink:#555555;
  --ink-dark:#3f3f3f;
  --muted:#8a8a8a;
  --blue:#1b8ed6;
  --blue-dark:#0f6fb5;
  --blue-box:#1a7ccb;
  --orange:#f7861b;
  --orange-dark:#e4660a;
  --red:#e9532c;
  --footer:#333333;
  --link:#1477c4;
}
*{margin:0;padding:0;box-sizing:border-box}
html,body{width:1152px;height:1200px;overflow:hidden}
body{
  position:relative;
  background:linear-gradient(var(--page-top) 0,var(--page-top) 970px,var(--page-bg) 970px);
  font-family:"Arimo",Arial,sans-serif;color:var(--ink);
}
.abs{position:absolute}
.sheet{left:106px;top:0;width:940px;height:1061px;background:var(--panel);border:1px solid var(--line);border-top:8px solid #6b6b6b}
.brand{left:117px;top:38px;display:flex;align-items:center;gap:10px}
.brand-mark{width:50px;height:50px;background:#6d6d6d;border-radius:4px}
.brand-name{font-family:"Roboto Condensed",sans-serif;font-weight:700;font-size:30px;color:#6d6d6d}
.btn{display:flex;align-items:center;justify-content:center;color:#fff;font-family:"Roboto Condensed",sans-serif;text-transform:uppercase}
.btn-orange{background:linear-gradient(#ffa23a,var(--orange-dark));border-radius:3px}
.top-join{left:857px;top:21px;width:106px;height:30px;font-size:15px}
.top-login{left:972px;top:21px;width:67px;height:30px;font-size:15px}
.search{left:811px;top:75px;width:226px;height:28px;border:1px solid #d2d2d2;border-radius:14px;font-size:13px;color:#aaa;padding:6px 12px;background:#fff}
.search svg{position:absolute;right:10px;top:6px}
.nav{left:115px;top:112px;width:922px;height:42px;background:linear-gradient(#27a0e6,var(--blue));display:flex;overflow:hidden}
.nav a{display:flex;align-items:center;justify-content:center;flex:none;color:#fff;font-family:"Roboto Condensed",sans-serif;font-size:11.5px;text-decoration:none;border-right:1px solid rgba(0,0,0,.15);white-space:nowrap}
.nav a:last-child{border-right:0;flex:1}
.hero{left:115px;top:154px;width:922px;height:336px;background:linear-gradient(100deg,#2b73c4 0%,#6aa7e3 45%,#c5dcf3 70%,#e8eff7 100%)}
.hero-box{left:207px;top:221px;width:478px;height:187px;background:var(--blue-box);text-align:center;color:#fff;font-family:"Roboto Condensed",sans-serif;padding-top:14px}
.hero-box h1{font-size:31px;font-weight:700;letter-spacing:.2px}
.hero-box p{font-size:18px;font-weight:700;line-height:21px;margin-top:8px}
.hero-join{position:absolute;left:162px;top:128px;width:146px;height:42px;font-size:18px;font-weight:700}
.dots{left:556px;top:469px;display:flex;gap:6px}
.dots span{width:9px;height:9px;border-radius:50%;background:#9aa6b2}
.dots span.on{background:#2c2c2c}
.newbie{left:115px;top:491px;width:922px;height:58px;border:1px solid var(--line);background:#fff}
.newbie p{position:absolute;left:16px;top:20px;font-family:"Roboto Condensed",sans-serif;font-size:17px;color:var(--ink-dark)}
.click{left:883px;top:497px;width:144px;height:43px;background:linear-gradient(#2aa2ea,var(--blue-dark));font-size:20px;font-weight:700;border-radius:2px}
.signal{left:115px;top:560px;width:924px;height:53px;border:1px solid var(--line);background:#fff;display:flex}
.signal-label{width:214px;height:53px;margin:-1px 0 0 -1px;flex:none}
.signal-cell{display:flex;align-items:center;justify-content:center;font-family:"Roboto Condensed",sans-serif;font-size:17px;color:#666;border-right:1px solid var(--line)}
.signal-cell:last-child{border-right:0}
.card{top:626px;width:289px;height:182px;border:1px solid #e2e2e2;background:#fff}
.card h2{height:38px;background:#efefef;font-family:"Roboto Condensed",sans-serif;font-weight:400;font-size:18px;color:var(--ink-dark);padding:9px 11px}
.card p{font-size:11px;line-height:16.3px;text-align:justify;padding:10px 9px 0 9px}
.card p+p{padding-top:0;margin-top:16px}
.more{position:absolute;left:9px;top:144px;width:77px;height:29px;background:var(--red);color:#fff;font-size:11px;display:flex;align-items:center;justify-content:center;border:1px solid #fff;outline:1px solid #e0e0e0}
.col-title{font-family:"Roboto Condensed",sans-serif;font-size:19px;color:var(--ink-dark);font-weight:400}
.col-text{font-size:11.5px;line-height:16.3px;text-align:justify}
.news-link{color:var(--link);font-size:13.5px}
.disclaimer{left:130px;top:1077px;width:892px;text-align:center;font-size:10.2px;line-height:12.6px;color:#8f8f8f}
.footer{left:0;top:1162px;width:1152px;height:38px;background:var(--footer)}
.footer p{position:absolute;left:102px;top:12px;color:#fff;font-family:"Open Sans",sans-serif;font-size:10.5px}
.social{position:absolute;right:110px;top:7px;display:flex;gap:11px}
.social span{width:24px;height:24px;border-radius:4px}
</style>
</head>
<body>
<div class="abs sheet"></div>

<div class="abs brand"><span class="brand-mark"></span><span class="brand-name">BrightCoinDesk.info</span></div>
<div class="abs btn btn-orange top-join">Join us free</div>
<div class="abs btn btn-orange top-login">Login</div>
<div class="abs search">Search
  <svg width="14" height="14" viewBox="0 0 14 14"><circle cx="5.5" cy="5.5" r="4" fill="none" stroke="#888" stroke-width="1.6"/><line x1="8.5" y1="8.5" x2="13" y2="13" stroke="#888" stroke-width="2"/></svg>
</div>

<nav class="abs nav">
  <a style="width:132px">ENTER TRADING ROOM</a><a style="width:67px">FORUM</a><a style="width:111px">CONTROL PANEL</a><a style="width:101px">FOREX ADVICE</a><a style="width:175px">LIVE FOREX TRADING SIGNALS</a><a style="width:114px">BROKER REVIEWS</a><a style="width:149px">BECOME A TEAM TRADER</a><a>CONTACT</a>
</nav>

<div class="abs hero" role="img" aria-label="Photo of a smiling trader in front of a blue stock ticker board"></div>
<div class="abs hero-box">
  <h1>FOLLOW PROFESSIONAL TRADERS</h1>
  <p>DID YOU KNOW YOU CAN COPY TRADES<br>AUTOMATICALLY INTO YOUR ACCOUNT USING OUR<br>SPECIAL SOFTWARE?</p>
  <div class="btn btn-orange hero-join">Join us free!</div>
</div>
<div class="abs dots"><span></span><span class="on"></span><span></span></div>

<div class="abs newbie"><p>ARE YOU A TOTAL NEWBIE? LET US SHOW YOU HOW TO GET START TRADING FOREX PROFITABLY TODAY!</p></div>
<div class="abs btn click">Click here</div>

<div class="abs signal">
  <svg class="signal-label" viewBox="0 0 214 53"><polygon points="0,0 190,0 214,26.5 190,53 0,53" fill="#e9532c"/><text x="19" y="35" fill="#fff" font-family="Roboto Condensed, sans-serif" font-size="22" font-weight="700">LATEST SIGNAL</text></svg>
  <div class="signal-cell" style="width:254px">SELL - USDJPY</div>
  <div class="signal-cell" style="width:260px">OPEN PRICE: 98.0990</div>
  <div class="signal-cell" style="flex:1">2 HOURS AGO</div>
</div>

<section class="abs card" style="left:115px">
  <h2>WHO ARE WE?</h2>
  <p>We are traders who are growing substantial wealth through trading Forex (Foreign Exchange).</p>
  <p>We leverage off successful strategies and systems found across the internet to find the few profitable</p>
  <span class="more">READ MORE</span>
</section>
<section class="abs card" style="left:432px">
  <h2>HOW DO WE DO IT?</h2>
  <p>We leverage off successful strategies and systems found across the internet to find the few profitable methods of making money in Forex and share that knowledge with our members through free forex trading signals displayed within our live trading room.</p>
  <span class="more">READ MORE</span>
</section>
<section class="abs card" style="left:749px">
  <h2>IS IT FREE?</h2>
  <p>YES! The trading signals are displayed live within the Forex Trading Room completely free of charge. You will also have the opportunity to discuss trade opportunities with our professional Team Traders in real time.</p>
  <span class="more">READ MORE</span>
</section>

<h2 class="abs col-title" style="left:115px;top:826px">WELCOME</h2>
<div class="abs col-text" style="left:115px;top:862px;width:606px">
  <p>My name is Sam Porter and I'm the owner and founder of BrightCoinDesk.info. I created this site to reach out to all the retail forex traders in the world who are struggling to trade profitably.</p>
  <p style="margin-top:16px">Here we give you the opportunity to connect with full time, professional forex traders and copy their signals inside our free forex trading room.I have extensive experience trading the forex market, however my true passion lies in building relationships with other talented and experienced traders across the globe and then benefiting from the profitable trading opportunities they identify by copying their trades.I make money by following forex traders who have the time, knowledge and skills needed to battle the market each day, and I share this opportunity with our members through the free forex trading room and automated forex signal copier.Please drop into the trading room so I can give you a tour and show you how you can make money following our team of forex traders.</p>
</div>

<h2 class="abs col-title" style="left:750px;top:826px">LATEST NEWS</h2>
<div class="abs news-link" style="left:750px;top:862px">How Does This Room Work?</div>
<p class="abs col-text" style="left:750px;top:895px;width:287px">YES! The trading signals are displayed live within the Forex Trading Room completely free of charge. You will also have the opportunity to discuss trade opportunities with our professional Team Traders in real time. We also provide trading activity from several third party signal providers and commercial EA's. Every forex strategy, signal and EA used on this site has a full REAL MONEY history available for review.</p>

<p class="abs disclaimer">Caution:Trading involves the possibility of financial loss. Only trade with money that you are prepared to lose, you must recognise that for factors outside your control you may lose all of the money in your trading account. Many forex brokers also hold you liable for losses that exceed your trading capital. So you may stand to lose more money than is in your account. BrightCoinDesk.info takes not responsibility for loss incurred as a result of our trading signals. By signing up as a member you acknowledge that we are not providing financial advice and that you are making a the decision to copy our trades on your own account. We have no knowledge on the level of money you are trading with or the level of risk you are taking with each trade. You must make your own financial decisions, we take no responsibility for money made or lost as a result of our signals or advice on forex related products on this website.</p>

<footer class="abs footer">
  <p>COPYRIGHT © 2012 brightcoindesk &nbsp;| All Rights Reserved.</p>
  <div class="social">
    <span style="background:#3b66b0"></span>
    <span style="background:#34a9e4"></span>
    <span style="background:#d9462b"></span>
    <span style="background:#f08a1d"></span>
  </div>
</footer>
</body>
</html>
```